Redesign of my Homepage - Online resource for anyone to learn American Sign Language

I would like to have a new homepage design http://www.HandwiseLessons.example . My business is a website for anyone to learn American Sign Language. There are over 300 video lessons, with each lesson having 20 vocabulary words, retention exercises, 16,000 video dictionary etc. It is a very extensive site. It is a self paced website. If you need a log in to see what customers see, please let me know. I would like to keep the same color scheme. I want the website to look modern and clean. I want a fresh look! I want something that is easy to navigate, attracts customers, and easy to follow. I would like the final design to communicate that my website is for anyone to learn how to sign with this incredible program.

Target Market(s)

Students taking American Sign Language, Parents with Deaf children, future interpreters for the deaf, co-workers of the Deaf. Also, schools that offer American Sign Language (online schools, homeschools, etc. ).

Industry/Entity Type

Business

Number of Pages Required

1 page

Requirements
Must have
• My project must be very clean and clear. I want my homepage to show that this is a program for people to learn how American Sign Language.
Nice to have
• Not sure. Surprise me.

```html
<!DOCTYPE html>
<html lang="en">
<head>
<meta charset="utf-8">
<title>Handwise Lessons — Learn ASL online</title>
<link href="https://fonts.googleapis.com/css2?family=Lato:wght@400;700;900&family=Roboto+Condensed:wght@300;400&family=Arimo&display=swap" rel="stylesheet">
<style>
:root{
  --green:#078a1c;
  --green-text:#0b8a1f;
  --grey-btn:#b8b8b8;
  --body-grey:#5d5d5d;
  --nav-grey:#444;
  --white:#fff;
}
*{margin:0;padding:0;box-sizing:border-box}
html,body{width:1141px;height:1200px;overflow:hidden;background:var(--white)}
body{position:relative;font-family:"Lato",sans-serif}
.topbar{position:absolute;left:0;top:0;width:1141px;height:39px;background:var(--green);color:var(--white);font-size:12px;font-family:"Lato",sans-serif}
.topbar .social{position:absolute;left:762px;top:14px;display:flex;gap:14px}
.topbar .social span{width:11px;height:11px;border-radius:50%;background:var(--white);display:block}
.topbar .account{position:absolute;left:874px;top:13px;display:flex;gap:10px;align-items:center}
.topbar .account svg{display:block}
.header{position:absolute;left:0;top:39px;width:1141px;height:87px;background:var(--white)}
.brand{position:absolute;left:104px;top:33px;display:flex;align-items:center;gap:6px;color:var(--green-text);font-weight:700;font-size:16px;white-space:nowrap}
.brand i{width:12px;height:12px;background:var(--green-text);display:block}
.nav{position:absolute;left:292px;top:42px;display:flex;gap:14px;font-family:"Roboto Condensed",sans-serif;font-weight:300;font-size:14px;color:var(--nav-grey);letter-spacing:-.1px;white-space:nowrap}
.nav .active{color:var(--green-text)}
.nav .drop::after{content:"";display:inline-block;margin-left:3px;border:4px solid transparent;border-top:5px solid #999;vertical-align:-2px}
.hero{position:absolute;left:0;top:126px;width:1141px;height:433px;background:linear-gradient(90deg,#8a7a5e 0%,#b26a52 25%,#c0343d 45%,#6c6a58 65%,#5b5a50 100%)}
.hero h1{position:absolute;left:697px;top:142px;color:var(--white);font-size:38px;font-weight:700;white-space:nowrap}
.hero p{position:absolute;left:700px;top:192px;width:360px;color:var(--white);font-size:19px;line-height:27px}
.btn{position:absolute;display:flex;align-items:center;justify-content:center;border-radius:20px;color:var(--white);font-weight:700;font-size:14px;background:var(--green);white-space:nowrap}
.btn.muted{background:var(--grey-btn)}
.hero .btn{left:805px;top:264px;width:116px;height:33px}
.card h2{position:absolute;color:var(--green-text);font-size:27px;font-weight:700;line-height:36px}
.card .photo{position:absolute;width:273px;height:109px}
.card p{position:absolute;width:290px;font-family:"Arimo",sans-serif;font-size:17px;line-height:24px;color:var(--body-grey)}
.card .btn{width:145px;height:39px}
.footer{position:absolute;left:0;top:978px;width:1141px;height:222px;background:var(--green);color:var(--white);text-align:center;font-size:13.5px;line-height:19px}
.footer .about{position:absolute;left:0;width:100%;top:50px}
.footer .links{position:absolute;left:0;width:100%;top:126px}
.footer .legal{position:absolute;left:0;width:100%;top:154px}
</style>
</head>
<body>
<div class="topbar">
  <div class="social"><span></span><span></span><span></span><span></span></div>
  <div class="account">
    <span>|</span>
    <svg width="10" height="11" viewBox="0 0 10 11"><circle cx="5" cy="3" r="2.6" fill="#fff"/><path d="M0 11c0-3.5 2-5 5-5s5 1.5 5 5z" fill="#fff"/></svg>
    <span>Login</span><span>|</span><span>Register</span><span>|</span>
    <svg width="11" height="11" viewBox="0 0 11 11"><circle cx="4.5" cy="4.5" r="3.3" fill="none" stroke="#fff" stroke-width="1.6"/><path d="M7 7l3 3" stroke="#fff" stroke-width="1.8"/></svg>
  </div>
</div>
<header class="header">
  <div class="brand"><i></i>Handwise Lessons</div>
  <nav class="nav">
    <span class="active">HOME</span>
    <span class="drop">HOW IT WORKS</span>
    <span>GIFT CERTIFICATES</span>
    <span>TRY IT FREE</span>
    <span>BUY NOW</span>
    <span class="drop">CONTACT US</span>
    <span>GROUP RATE FORM</span>
    <span>TEACHER'S GUIDE</span>
  </nav>
</header>
<section class="hero" role="img" aria-label="Photo of a mother signing to her young son outdoors, with another child nearby">
  <h1>Lean ASL online</h1>
  <p>Duis sed odio sit amet nibh vulputate cursus a sit amet mauris.</p>
  <span class="btn">TRY IT FREE</span>
</section>
<section class="card">
  <h2 style="left:107px;top:610px;width:300px">Learning Community</h2>
  <div class="photo" role="img" aria-label="Photo of a girl signing in a classroom" style="left:94px;top:680px;background:linear-gradient(90deg,#5a4030,#b89a70,#d8c8a0)"></div>
  <p style="left:103px;top:802px">Anyone that has a passion to learn American Sign Language (ASL)</p>
  <span class="btn" style="left:167px;top:875px">+ LEARN MORE</span>
</section>
<section class="card">
  <h2 style="left:436px;top:598px;width:260px">Hearing parents of deaf children</h2>
  <div class="photo" role="img" aria-label="Photo of parents practising signs together" style="left:436px;top:680px;background:linear-gradient(90deg,#6a5040,#3d6f78,#c49a80)"></div>
  <p style="left:435px;top:802px">Learn to communicate more effectively with your child</p>
  <span class="btn muted" style="left:500px;top:875px">+ LEARN MORE</span>
</section>
<section class="card">
  <h2 style="left:776px;top:598px;width:240px">Deaf and hard of hearing</h2>
  <div class="photo" role="img" aria-label="Photo of a teacher and child signing in a colourful classroom" style="left:774px;top:680px;background:linear-gradient(90deg,#4a3a3a,#5a6a9a,#d04a50,#2f6a40)"></div>
  <p style="left:774px;top:802px">Learn to tackle the challenges you faced in the classroom</p>
  <span class="btn muted" style="left:839px;top:875px">+ LEARN MORE</span>
</section>
<footer class="footer">
  <p class="about">Handwise Lessons is a subscription based website for American Sign Language (ASL). The content is for anyone who wishes<br>to learn ASL, regardless of age. It has been designed to instruct deaf students, parents of deaf children, and the community-at-large.<br>You may cancel your subscription at any time. All lessons are taught by Deaf experts of ASL.</p>
  <p class="links">Contact Us | Our Mission | Terms &amp; Conditions</p>
  <p class="legal">HandwiseLessons ©2017 All Rights Reserved | 1485286365.6586s</p>
</footer>
</body>
</html>
```